Webdesign for Brightwell for use on webpage

We aim to deliver insights for power consumers in the nordic market in the B2B market, without being a supplier.

Since we are helping customers in the green transition and reducing CO2 emissions, green colors would be preferred, but we are keeping an open mind. We would like to communicate transperancy, awareness and enabling economic potential for customers.

We deliver our product on a SaaS platform through visualization in dashboards

Target Market(s)

B2B

Industry/Entity Type

Power Consumption

Number of Pages Required

1 page

Colors
0054AA
0677BA
7BADD7
CADEEF
E8F1F8
0094D4
00A9DD
6FCCEA
C7EBF8
E9F6FB
00AB8E
00BBA5
67D7C9
C6EFE9
E9F9F6
59FF00
82FF00
B8FF75
E3FFCB
F4FFEA

Requirements
Must have
• The general looks and color schemes must be in line with logo called "brightwell.eps" - see attached

```html
<!DOCTYPE html>
<html lang="en">
<head>
<meta charset="utf-8">
<title>Brightwell – Energy data insights</title>
<link rel="stylesheet" href="https://fonts.googleapis.com/css2?family=Montserrat:wght@400;500;700&display=swap">
<style>
:root{
  --green:#8cc63f;
  --blue:#0000ff;
  --ink:#222;
  --white:#fff;
  --mist:#e8edf3;
  --line:#dcdcdc;
  --smoke-dark:#5a4a36;
  --smoke-light:#c9a878;
}
*{box-sizing:border-box;margin:0;padding:0}
html,body{width:1200px;height:1200px;overflow:hidden;background:var(--white)}
body{font-family:"Montserrat",Arial,sans-serif;color:var(--ink);position:relative}
.page{position:absolute;left:287px;top:0;width:573px;height:1194px;border-left:1px solid var(--line);border-right:1px solid var(--line)}
.abs{position:absolute}
.hero{left:0;top:0;width:573px;height:186px;background:linear-gradient(160deg,#8a7458 0%,#c9a878 35%,#e3d3b8 55%,#7b6a58 80%,#3b3129 100%)}
.nav{top:11px;font-size:4.5px;color:var(--white);letter-spacing:.1px}
.brand-mark{width:44px;height:44px;border:2px solid var(--white);border-radius:50%}
.brand-name{font-weight:700;color:var(--white);letter-spacing:.5px}
.hero-title{left:139px;top:117px;font-size:15px;color:var(--white);font-weight:400}
.hero-text{left:139px;top:149px;width:290px;font-size:7.3px;line-height:9.4px;color:var(--white)}
.section-title{width:573px;text-align:center;left:0}
.challenge{width:95px;height:187px;top:256px}
.challenge p{position:absolute;right:8px;bottom:8px;width:76px;text-align:right;font-size:7.2px;line-height:8.4px;color:var(--white)}
.band{left:0;top:486px;width:573px;height:35px;background:var(--green)}
.band p{position:absolute;right:176px;top:7px;width:260px;text-align:right;font-size:7px;line-height:8.5px;color:var(--white)}
.co2{left:0;top:521px;width:573px;height:150px;background:linear-gradient(100deg,#f5a623 0%,#e9b35a 18%,#4d6f9c 42%,#3f5f8e 60%,#e8955a 80%,#f0b070 100%)}
.check{width:12px;height:12px}
.point{font-size:5.8px;line-height:7.7px;color:var(--white);width:115px}
.btn{background:var(--blue);color:var(--white);text-align:center;font-size:5.2px}
.services{left:0;top:671px;width:573px;height:139px;background:var(--green)}
.service-icon{width:38px;height:38px;border-radius:50%;background:radial-gradient(circle at 35% 30%,#d8d8d8,#7a7a7a 70%,#555)}
.service-label{width:60px;text-align:center;font-size:5.6px;line-height:6.6px;color:#2a3a1a}
.testimonials{left:0;top:810px;width:573px;height:216px;background:var(--mist)}
.card{top:76px;width:92px;height:116px;background:var(--white);border-bottom:2px solid var(--blue)}
.card p{position:absolute;left:6px;top:10px;width:80px;text-align:center;font-family:Arial,sans-serif;font-size:5.2px;line-height:9.4px;color:#333}
.avatar{left:10px;top:92px;width:17px;height:16px;background:linear-gradient(135deg,#3f7f4a,#c9d9c0)}
.who{left:33px;top:92px;font-family:Arial,sans-serif;font-size:6px;color:#222}
.who small{display:block;font-size:3.6px;color:#888;margin-top:1px}
.dot{top:202px;width:6px;height:2.5px;background:#222}
.join{left:0;top:1026px;width:573px;height:168px;background:linear-gradient(120deg,#6f9a3a 0%,#3f6a2a 30%,#aac37a 55%,#5d7d36 75%,#2f4a22 100%)}
.field{background:var(--white);font-family:Arial,sans-serif;font-size:4.2px;color:#aaa;padding:1px 2px}
.social{width:10px;height:10px;border:1px solid var(--white);border-radius:50%}
</style>
</head>
<body>
<div class="page">
  <header class="abs hero" role="img" aria-label="Photo of an industrial plant with smoke stacks under heavy clouds">
    <span class="abs nav" style="left:293px">SERVICES</span>
    <span class="abs nav" style="left:332px">FEATURES</span>
    <span class="abs nav" style="left:363px">TESTIMONIALS</span>
    <span class="abs nav" style="left:414px">CONTACT</span>
    <div class="abs brand-mark" style="left:160px;top:37px"></div>
    <span class="abs brand-name" style="left:135px;top:84px;font-size:13px;width:94px;text-align:center">BRIGHTWELL</span>
  </header>
  <h1 class="abs hero-title">LOREM IPSUM SIT AMET</h1>
  <p class="abs hero-text">Lorem ipsum dolor sit amet, consectetur adipiscing elit. Vivamus fermentum risus quis velit scelerisque hendrerit. Phasellus vel mattis est. Maecenas lacinia neque ut lacinia scelerisque.</p>

  <h2 class="abs section-title" style="top:218px;font-size:11px;font-weight:400">What We Face Together</h2>
  <div class="abs challenge" style="left:139px;background:linear-gradient(180deg,#c98a2a,#5a3a1a 60%,#1e1a16)" role="img" aria-label="Photo of factory chimneys releasing dark smoke"><p>Cras nisl leo, porttitor eu iaculis eget ornare elementum nisltor euleo aliquet</p></div>
  <div class="abs challenge" style="left:242px;background:radial-gradient(circle at 55% 65%,#b5562a,#3a1d14 55%,#140c0a)" role="img" aria-label="Photo of a man holding a glowing light bulb"><p>Cras nisl leo, porttitor eu iaculis eget ornare elementum nisltor euleo aliquet</p></div>
  <div class="abs challenge" style="left:345px;background:radial-gradient(circle at 50% 30%,#4ea83a,#1d5a22 55%,#0b2a12)" role="img" aria-label="Photo of a green leaf floating above an open hand"><p>Cras nisl leo, porttitor eu iaculis eget ornare elementum nisltor euleo aliquet</p></div>

  <div class="abs band">
    <p>Cras nisl leo, porttitor eu iaculis eget ornare elementum nisltor euleo aliquet</p>
    <div class="abs" style="left:412px;top:3px;width:17px;height:17px;border:1px solid var(--white);border-radius:50%"></div>
    <span class="abs brand-name" style="left:398px;top:21px;font-size:5px;width:46px;text-align:center">BRIGHTWELL</span>
  </div>

  <section class="abs co2" role="img" aria-label="Photo of smoke stacks with blue smoke against an orange sunset sky">
    <h2 class="abs section-title" style="top:11px;font-size:11px;font-weight:400;color:var(--white)">SOLVE CO2 PROBLEMS</h2>
    <p class="abs section-title" style="top:30px;font-size:9px;color:var(--white)">hendrerit et massa</p>
    <svg class="abs check" style="left:145px;top:60px" viewBox="0 0 12 12"><circle cx="6" cy="6" r="6" fill="#fff"/><path d="M3 6.2l2 2 4-4.2" stroke="#4d6f9c" stroke-width="1.5" fill="none"/></svg>
    <p class="abs point" style="left:161px;top:59px">Nulla sed condimentum nisl, ut molestie mi. Vivamus pharetra elit sit amet massa matti.</p>
    <svg class="abs check" style="left:145px;top:86px" viewBox="0 0 12 12"><circle cx="6" cy="6" r="6" fill="#fff"/><path d="M3 6.2l2 2 4-4.2" stroke="#4d6f9c" stroke-width="1.5" fill="none"/></svg>
    <p class="abs point" style="left:161px;top:85px">Proin tempor malesuada sem, eu interdum tempor ipsum imperdiet</p>
    <svg class="abs check" style="left:296px;top:60px" viewBox="0 0 12 12"><circle cx="6" cy="6" r="6" fill="#fff"/><path d="M3 6.2l2 2 4-4.2" stroke="#4d6f9c" stroke-width="1.5" fill="none"/></svg>
    <p class="abs point" style="left:311px;top:59px">Proin tempor malesuada sem, eu interdum tempor ipsum imperdiet</p>
    <svg class="abs check" style="left:296px;top:86px" viewBox="0 0 12 12"><circle cx="6" cy="6" r="6" fill="#fff"/><path d="M3 6.2l2 2 4-4.2" stroke="#4d6f9c" stroke-width="1.5" fill="none"/></svg>
    <p class="abs point" style="left:311px;top:85px">Nulla sed condimentum nisl, ut molestie mi. Vivamus pharetra elit sit amet massa matti.</p>
    <div class="abs btn" style="left:237px;top:123px;width:99px;height:12px;line-height:12px">CRAS CONGUE DAPIBUS CURSUS</div>
  </section>

  <section class="abs services">
    <h2 class="abs section-title" style="top:12px;font-size:11px;font-weight:400;color:var(--white)">OUR SERVICES</h2>
    <div class="abs service-icon" style="left:146px;top:41px" role="img" aria-label="Photo of a wind turbine"></div>
    <p class="abs service-label" style="left:135px;top:84px">Donec fringilla ipsum rhoncus porta</p>
    <div class="abs service-icon" style="left:213px;top:41px" role="img" aria-label="Photo of a wind turbine"></div>
    <p class="abs service-label" style="left:202px;top:84px">Curabitur laoreet libero sed</p>
    <div class="abs service-icon" style="left:268px;top:41px" role="img" aria-label="Photo of a wind turbine"></div>
    <p class="abs service-label" style="left:257px;top:84px">Sed interdum pharetra lacus</p>
    <div class="abs service-icon" style="left:323px;top:41px" role="img" aria-label="Photo of a wind turbine"></div>
    <p class="abs service-label" style="left:307px;top:84px;width:70px">Vivamus vestibulum massa</p>
    <div class="abs service-icon" style="left:391px;top:41px" role="img" aria-label="Photo of a wind turbine"></div>
    <p class="abs service-label" style="left:380px;top:84px">Maecenas nec vehicula eros</p>
  </section>

  <section class="abs testimonials">
    <div class="abs" style="left:276px;top:9px;width:21px;height:21px;border:1.5px solid #0054aa;border-radius:50%"></div>
    <span class="abs" style="left:246px;top:32px;width:81px;text-align:center;font-weight:700;font-size:7px;color:#0054aa">BRIGHTWELL</span>
    <h2 class="abs section-title" style="top:49px;font-size:9.5px;font-weight:400">TESTIMONIALS</h2>
    <div class="abs card" style="left:139px"><p>Lorem ipsum dolor sit amet, consectetur adipiscing elit. Maecenas dapibus mi neque, at tempus lacus interdum a. Donec id euismod purus. Duis nec mauris efficitur, pharetra arcu ut ...</p><div class="abs avatar" role="img" aria-label="Portrait photo of the reviewer"></div><div class="abs who">Marin Doe<small>Digital Marketing Executive</small></div></div>
    <div class="abs card" style="left:241px"><p>Lorem ipsum dolor sit amet, consectetur adipiscing elit. Maecenas dapibus mi neque, at tempus lacus interdum a. Donec id euismod purus. Duis nec mauris efficitur, pharetra arcu ut ...</p><div class="abs avatar" role="img" aria-label="Portrait photo of the reviewer"></div><div class="abs who">Marin Doe<small>Digital Marketing Executive</small></div></div>
    <div class="abs card" style="left:342px"><p>Lorem ipsum dolor sit amet, consectetur adipiscing elit. Maecenas dapibus mi neque, at tempus lacus interdum a. Donec id euismod purus. Duis nec mauris efficitur, pharetra arcu ut ...</p><div class="abs avatar" role="img" aria-label="Portrait photo of the reviewer"></div><div class="abs who">Marin Doe<small>Digital Marketing Executive</small></div></div>
    <div class="abs dot" style="left:274px;background:var(--blue)"></div>
    <div class="abs dot" style="left:283px"></div>
    <div class="abs dot" style="left:292px"></div>
  </section>

  <section class="abs join" role="img" aria-label="Photo of a mossy forest floor with ferns">
    <div class="abs" style="left:149px;top:14px;width:26px;height:26px;border:1.5px solid var(--white);border-radius:50%"></div>
    <span class="abs brand-name" style="left:135px;top:42px;width:56px;font-size:7px;text-align:center">BRIGHTWELL</span>
    <h2 class="abs" style="left:191px;top:14px;font-size:11px;font-weight:400;color:var(--white)">JOIN US!</h2>
    <p class="abs" style="left:191px;top:38px;font-size:11px;color:var(--white)">Pellentesque rutrum turpis id blandt</p>
    <div class="abs field" style="left:140px;top:59px;width:92px;height:10px">Your Name</div>
    <div class="abs field" style="left:242px;top:59px;width:92px;height:10px">Your Email</div>
    <div class="abs field" style="left:344px;top:59px;width:92px;height:10px">Your Phone</div>
    <div class="abs field" style="left:140px;top:76px;width:296px;height:50px;padding-top:2px">Your Message</div>
    <div class="abs btn" style="left:253px;top:133px;width:70px;height:13px;line-height:13px">SEND MESSAGE</div>
    <div class="abs social" style="left:381px;top:135px"></div>
    <div class="abs social" style="left:395px;top:135px"></div>
    <div class="abs social" style="left:409px;top:135px"></div>
    <div class="abs social" style="left:423px;top:135px"></div>
  </section>
</div>
</body>
</html>
```